Update our OBGYN business card look and info

We are an OBGYN office. Our logo is nice but would like to "woman" part of the logo to be a darker color, to contrast with the flower that surrounds it. Maybe make our practice name Bloom Circle Health more feminine. Our practice caters to women only. All providers and staff are female.

Target Market(s)

Females 16-65.

Industry/Entity Type

Business

Contact Information for Business Card

See attached upload. The ONLY CHANGE to the information is DELETE the name Marla Quenbright, Midwife and REPLACE with Tessa Dravinoux, Midwife

Logo Text

Bloom Circle Health Obstetrics & Gynecology

Font styles to use
Serif
Script

Colors
85cae6
0692cd
33a6d7
85abd2
f59195
eea4c8
cadf82
fac994
d3a5cc

```html
<!DOCTYPE html>
<html lang="en">
<head>
<meta charset="utf-8">
<title>Bloom Circle Health – Business Card</title>
<link rel="stylesheet" href="https://fonts.googleapis.com/css2?family=Cormorant+Garamond:ital,wght@0,600;1,600&family=Roboto:wght@400&family=Tinos&display=swap">
<style>
  :root {
    --page: #e9ebed;
    --card: #ffffff;
    --sky: #86c3d4;
    --coral: #ec6a5e;
    --slate: #5d5d60;
    --ink: #1d1d1f;
  }
  * { box-sizing: border-box; margin: 0; padding: 0; }
  html, body { width: 1200px; height: 900px; overflow: hidden; background: var(--page); }
  .canvas { position: relative; width: 1200px; height: 900px; }

  .card {
    position: absolute;
    width: 640px; height: 366px;
    background: var(--card);
    border-radius: 22px;
    overflow: hidden;
    box-shadow: 0 10px 28px rgba(0,0,0,.18);
  }
  .card--back { left: 500px; top: 60px; }
  .card--front { left: 70px; top: 470px; }

  .card__waves { position: absolute; inset: 0; }

  /* brand lockup */
  .brand { position: absolute; display: flex; align-items: center; gap: 14px; }
  .brand__dot { border-radius: 50%; background: var(--sky); flex: none; }
  .brand__name {
    font-family: "Cormorant Garamond", Georgia, serif;
    font-weight: 600;
    color: var(--slate);
    white-space: nowrap;
  }
  .card--front .brand { left: 34px; top: 26px; }
  .card--front .brand__dot { width: 58px; height: 58px; }
  .card--front .brand__name { font-size: 42px; line-height: 1; }
  .brand__tagline {
    position: absolute; left: 108px; top: 74px;
    font-family: "Cormorant Garamond", Georgia, serif;
    font-style: italic; font-weight: 600;
    font-size: 23px; color: var(--coral);
  }

  .card--back .brand { left: 50%; top: 96px; transform: translateX(-50%); }
  .card--back .brand__dot { width: 74px; height: 74px; }
  .card--back .brand__name { font-size: 38px; }

  .back__url {
    position: absolute; left: 0; right: 0; top: 258px;
    display: flex; align-items: center; justify-content: center; gap: 22px;
    font-family: Roboto, Arial, sans-serif; font-size: 15px; color: var(--ink);
  }
  .back__url::before, .back__url::after {
    content: ""; width: 170px; height: 1px; background: var(--ink);
  }

  /* contact */
  .contact {
    position: absolute; left: 32px; top: 168px;
    font-family: Roboto, Arial, sans-serif; font-size: 15px; line-height: 21px; color: var(--ink);
    list-style: none;
  }
  .contact__row { display: flex; align-items: center; gap: 7px; }
  .contact__icon { width: 14px; height: 14px; flex: none; }

  .providers {
    position: absolute; right: 34px; bottom: 20px;
    text-align: right; list-style: none;
    font-family: Tinos, "Times New Roman", serif; font-size: 20px; line-height: 23px; color: var(--ink);
  }
</style>
</head>
<body>
<main class="canvas">

  <section class="card card--back" aria-label="Business card back">
    <div class="brand">
      <span class="brand__dot"></span>
      <span class="brand__name">Bloom Circle Health</span>
    </div>
    <p class="back__url">www.bloomcirclehealth.com</p>
  </section>

  <section class="card card--front" aria-label="Business card front">
    <svg class="card__waves" viewBox="0 0 640 366" preserveAspectRatio="none" aria-hidden="true">
      <path d="M0,112 C200,140 420,160 640,168" fill="none" stroke="var(--sky)" stroke-width="8"/>
      <path d="M0,130 C200,158 420,178 640,186" fill="none" stroke="var(--coral)" stroke-width="8"/>
      <path d="M0,150 C200,176 420,196 640,204 L640,366 L0,366 Z" fill="var(--sky)"/>
    </svg>

    <div class="brand">
      <span class="brand__dot"></span>
      <span class="brand__name">Bloom Circle Health</span>
    </div>
    <p class="brand__tagline">Obstetrics &amp; Gynecology</p>

    <ul class="contact">
      <li>2480 Larkspur Avenue, Suite 3B</li>
      <li>Brookhaven, GA 31990</li>
      <li class="contact__row">
        <svg class="contact__icon" viewBox="0 0 16 16" aria-label="Phone"><path d="M1 5c0-2 2-3 7-3s7 1 7 3v1h-4V5H5v1H1Z M3 8h10l1 6H2Z" fill="var(--ink)"/></svg>
        555-318-2204
      </li>
      <li class="contact__row">
        <svg class="contact__icon" viewBox="0 0 16 16" aria-label="Fax"><path d="M4 1h8v4H4Z M1 6h14v6h-3v3H4v-3H1Z" fill="var(--ink)"/><rect x="5" y="10" width="6" height="4" fill="var(--sky)"/></svg>
        555-318-2297
      </li>
      <li class="contact__row">
        <svg class="contact__icon" viewBox="0 0 16 16" aria-label="Website"><g fill="none" stroke="var(--ink)" stroke-width="1.3"><circle cx="8" cy="8" r="6.5"/><ellipse cx="8" cy="8" rx="3" ry="6.5"/><path d="M1.5 8h13M3 4.5h10M3 11.5h10"/></g></svg>
        www.bloomcirclehealth.com
      </li>
    </ul>

    <ul class="providers">
      <li>Renata Holloway, MD</li>
      <li>Dana Whitcombe, MD</li>
      <li>Lydia Ferrant, MD</li>
      <li>Maren Ashby, Midwife</li>
      <li>Tessa Dravinoux, Midwife</li>
    </ul>
  </section>

</main>
</body>
</html>
```